Professional Lawn Treatment flyer (double sided) needed for established gardening company

We are an established and trusted gardening company in Swindon, UK, and are about to launch a new Lawn Treatment Service. This will be marketed to both existing and new customers and needs to reflect our current professional image. The flyer will need to be double-sided, portrait orientation and correctly sized so to be printed on A5.

If you look on our website www.tavistrowgardening.co.uk, you will see our colours are purple and green. We would like you to use these exact shades of purple and green in your design.

As part of the design, we will need you to put together an infographic table to show our packages. I have attached a spreadsheet which explains these packages but I will need you to create a visually appealing table that fits in with the overall design of the flyer. I don't want you to simply cut and paste my basic table into the design.

In terms of what needs to be included, I have tried to be as specific as possible here but please feel free to message me if you need any further information or clarification.

FRONT SIDE:
The title of our service is:
Expert Lawn Treatment Service

Our strapline will need to be included somewhere:
"Lawn care by your local gardening expert"

The front side of the flyer will need to contain our logo - different versions of which can be found within my dropbox folder here...

https://www.sharebinnu.co.uk/sh/k7qd21mzplax/QRT8xWbnNeLu4Pa-ZxYyhKcLo?dl=0

The front side will need to contain a main image (although feel free to add more if you have anything suitable). I have included a picture in the dropbox folder titled "Front side image" which we would like used. I've also included in the folder an adobe image of grass which you may or may not like to use on either front or back.

Somewhere on both the front and back sides, you will need to include our contact details:
01632 960417
www.tavistrowgardening.co.uk/lawncare

The front side should show what treatments we currently have available. These are:

- Lawn Fertilising
- Scarification
- Aeration
- Weed Control
- Moss Control
- Hydration Booster
- PlumeRest
- Turfing & Renovation

"Select a one-off treatment or choose from one of our specially created lawn care packages."

BACK SIDE:
On the back, we will still need our logo and contact details but the image we'd like used should be the one in the dropbox folder titled "Back side image". Again, if you have any other images you feel would also work, then please feel free to add them.

The back side is to contain a bit more information and be a bit 'wordier' and so can you please include the following 2 paragraphs:

"As expert gardeners, we are passionate about horticulture and working to bring out the very best in your garden. When we work in your garden, we look at it and treat it with the same care and attention as if it were our own, before handing it back for you to enjoy. Our passion doesn't end at just trees and shrubs though. Your grass is as much of a living, breathing plant as your shrubs and we therefore utilise our expert horticultural knowledge to ensure your lawn thrives and reaches its fullest potential.

Lawn care isn't just about applying a fertiliser. It's about really understanding your lawn and being able to use extensive knowledge and experience to diagnose and treat issues. It therefore stands to reason that you should employ an expert to bring out the best in your lawn which is why we at Tavistrow Gardening Services have created a superior lawn care service that will keep your lawn looking lush, green and healthy all year round."

I referred at the very top of this brief to the fact we will need an infographic table created to show the different lawn care packages available. You see from the PDF table I created that we have 3 packages; Standard, Enhanced and Premium. Please create a visually appealing table which sets out the differences between our packages and include it on the back page.

Finally, somewhere we would like reference to the other gardening services we do. It's only to be something small as it isn't the main focus of the flyer but we think it would be good to mention what else we do. To re-iterate, it isnt to be big. I still want the main focus to be lawn care but if you could somehow reference that we also do the following services, that would be good. I will leave it to you to decide where on the flyer it fits in best, be it the front or back:

- Lawn mowing
- Shrub pruning
- Hedge trimming
- Weed killing
- Garden clearance & tidy-up
- Planting & design
- Regular Garden Maintenance
- Turfing
- Fencing
- Gutter clearance

I think thats it. I look forward to your designs!
Ps. Don't forget the dropbox folder:

Target Market(s)

Professional men/women aged 25+
Retired aged 65+

Industry/Entity Type

Home And Garden

Font styles to use
Sans Serif

Colors
6b449b
9bcb3c

Requirements
Must have
• Our company colours; purple and green; as per our website www.tavistrowgardening.co.uk. I've selected purple and green on this brief just to highlight the colours needed but please be sure to use the exact shades from our website and NOT the shade of purple and green that were selected on this brief.
• All the wording as explained in the main project brief.
Nice to have
• I want the flyer to be bold, eye-catching and modern.
• We particularly like the font Trebuchet MS for general copy but please feel free to use any other font for bolder, main titles.
Should not have
• We don't want anything gimmicky. No cheesy marketing.
• We only want professional looking designs. With the greatest of respect, if you're just starting out or don't really do design but think you'll use this as practise, please don't waste your or our time. We've previously run contests for other projects where we've had designs submitted that have clearly been done on MS Word and used Clipart and Wordart. That's really not what we are looking for.

```html
<!DOCTYPE html>
<html lang="en">
<head>
<meta charset="utf-8">
<title>Tavistrow Gardening Services – Lawn Treatment Flyer</title>
<link href="https://fonts.googleapis.com/css2?family=Montserrat:wght@500;600;700&family=Lato:ital,wght@0,400;0,700;1,400;1,700&family=Arimo:ital,wght@0,400;1,400;1,700&display=swap" rel="stylesheet">
<style>
  :root{
    --purple:#7b2082;
    --purple-soft:#9a4aa0;
    --green:#3cb44a;
    --green-light:#a9d98a;
    --lime:#9bcb3c;
    --brown:#3a2418;
    --ink:#3d3d3d;
    --paper:#f2f3f1;
    --stage:#e6e6e6;
    --white:#ffffff;
  }
  *{box-sizing:border-box;margin:0;padding:0}
  html,body{width:1200px;height:902px;overflow:hidden}
  body{background:var(--stage);font-family:"Lato",sans-serif;position:relative}

  .flyer{position:absolute;top:84px;width:520px;height:735px;overflow:hidden;
    background:radial-gradient(ellipse at 50% 60%,#fbfbfa 0%,var(--paper) 60%,#dfe1dd 100%);
    box-shadow:0 6px 18px rgba(0,0,0,.18)}
  .flyer--front{left:60px}
  .flyer--back{left:620px}
  .layer{position:absolute;inset:0;width:100%;height:100%}

  .photo{position:absolute}
  .brand{position:absolute;text-align:center;font-family:"Lato",sans-serif;font-weight:700;color:var(--brown);line-height:1.1}
  .brand__mark{display:block;width:26px;height:26px;border-radius:50%;background:var(--lime);margin:0 auto 8px}

  /* front */
  .front-photo{left:0;top:150px;width:520px;height:190px;
    background:linear-gradient(160deg,#6fa64a 0%,#8fc25c 35%,#d9d6cc 55%,#7db551 75%,#4f8a34 100%)}
  .front-brand{left:110px;top:40px;width:300px;font-size:30px}
  .inset{position:absolute;border-radius:50%;border:5px solid var(--purple);box-shadow:0 2px 6px rgba(0,0,0,.25)}
  .inset--turf{left:16px;top:236px;width:110px;height:110px;background:radial-gradient(circle at 40% 40%,#8cbf5a,#4b3a26 80%)}
  .inset--spreader{left:122px;top:268px;width:106px;height:106px;background:radial-gradient(circle at 50% 45%,#c83a2c 0%,#9fb47d 45%,#6d9a45 100%)}

  .headline{position:absolute;left:0;width:520px;text-align:center;font-family:"Montserrat",sans-serif;font-weight:700;letter-spacing:1px;line-height:1}
  .headline--top{top:390px;font-size:41px;color:var(--brown)}
  .headline--bottom{top:440px;font-size:41px;color:var(--green)}

  .offer-pill{position:absolute;left:67px;top:488px;width:386px;height:42px;border-radius:21px;
    background:var(--purple);border:2px solid #c9a3cc;box-shadow:0 2px 4px rgba(0,0,0,.25);
    color:var(--white);font-family:"Arimo",sans-serif;font-size:11.5px;font-weight:700;text-transform:uppercase;
    text-align:center;line-height:15px;padding-top:5px}

  .treatments{position:absolute;left:22px;top:548px;width:480px;display:grid;grid-template-columns:154px 160px 166px;row-gap:10px;list-style:none}
  .treatments li{display:flex;align-items:center;gap:8px;font-family:"Arimo",sans-serif;font-style:italic;font-size:12.5px;color:var(--ink);height:22px}
  .treatment-icon{width:22px;height:22px;flex:none}

  .contact{position:absolute;color:var(--white);font-family:"Arimo",sans-serif}
  .contact__row{display:flex;align-items:center;gap:7px}
  .contact__phone{font-size:16px}
  .contact__web{font-size:11px;margin-top:6px}
  .contact svg{flex:none}
  .front-contact{left:20px;top:648px}
  .strapline{position:absolute;left:318px;top:654px;width:190px;text-align:center;font-family:"Arimo",sans-serif;font-size:13px;color:var(--brown);line-height:17px}
  .grass{position:absolute;left:0;bottom:0;width:520px;height:38px;
    background:linear-gradient(180deg,rgba(120,190,60,0) 0%,#7ec23e 40%,#3f8f24 100%)}

  /* back */
  .back-photo{left:0;top:0;width:240px;height:190px;
    background:linear-gradient(135deg,#a9a193 0%,#6fae45 30%,#9cd062 50%,#5f9b3a 70%,#c7c0b2 100%)}
  .back-brand{left:260px;top:40px;width:230px;font-size:26px}
  .about{position:absolute;left:18px;top:222px;width:484px;font-family:"Lato",sans-serif;font-size:9.6px;line-height:11.6px;color:var(--ink);text-align:justify}
  .about p+p{margin-top:11px}

  .packages-title{position:absolute;left:52px;top:378px;width:426px;height:42px;border-radius:14px 14px 0 0;
    background:var(--purple);border:3px solid var(--white);border-bottom:none;box-shadow:0 -1px 4px rgba(0,0,0,.2);
    color:var(--white);font-family:"Montserrat",sans-serif;font-weight:600;font-size:18px;text-align:center;line-height:38px}
  .packages{position:absolute;left:24px;top:418px;width:472px;border-collapse:separate;border-spacing:0;
    border:2px solid #555;border-radius:8px;overflow:hidden;background:var(--white);font-family:"Arimo",sans-serif}
  .packages th{height:24px;font-size:8px;font-weight:400;color:#222;text-transform:uppercase;text-align:center}
  .packages th:first-child{text-align:left;padding-left:32px;font-size:10px;font-weight:700}
  .packages td{height:19px;font-size:10.5px;color:var(--white);text-align:center;border-bottom:1px solid var(--white)}
  .packages td:first-child{text-align:left;padding-left:8px;width:160px}
  .packages td+td{border-left:2px solid var(--white)}
  .packages tr:nth-child(odd) td:nth-child(1),.packages tr:nth-child(odd) td:nth-child(3){background:var(--purple)}
  .packages tr:nth-child(odd) td:nth-child(2),.packages tr:nth-child(odd) td:nth-child(4){background:var(--green)}
  .packages tr:nth-child(even) td:nth-child(1),.packages tr:nth-child(even) td:nth-child(3){background:var(--purple-soft)}
  .packages tr:nth-child(even) td:nth-child(2),.packages tr:nth-child(even) td:nth-child(4){background:var(--green-light)}
  .packages tbody tr:nth-child(even) td:first-child{color:var(--purple);background:var(--green-light)}
  .packages tbody tr:nth-child(even) td:nth-child(3){background:#b983bd}
  .tick{width:11px;height:9px;vertical-align:middle}

  .other-services{position:absolute;left:22px;top:620px;width:300px;font-family:"Arimo",sans-serif}
  .other-services h3{font-size:8.5px;font-weight:700;color:var(--purple);text-transform:uppercase;margin-bottom:7px}
  .other-services ul{list-style:none;display:grid;grid-template-columns:78px 118px 80px;grid-auto-flow:column;grid-template-rows:repeat(4,12px)}
  .other-services li{font-size:7.6px;font-style:italic;color:#333;display:flex;align-items:center;gap:5px}
  .other-services li::before{content:"";width:5px;height:5px;border-radius:50%;background:var(--green);flex:none}
  .back-contact{left:288px;top:668px}
  .back-contact .contact__phone{font-size:19px}
  .grass--back{width:280px}
</style>
</head>
<body>

<!-- FRONT -->
<section class="flyer flyer--front" aria-label="Flyer front">
  <div class="photo front-photo" role="img" aria-label="Photo of a striped green lawn with a curving stone garden path"></div>

  <svg class="layer" viewBox="0 0 520 735" aria-hidden="true">
    <path d="M0 0H520V220C470 250 380 262 260 262C140 262 40 230 0 200Z" fill="var(--purple)"/>
    <path d="M0 0H520V190C460 230 370 250 260 250C140 250 50 215 0 170Z" fill="var(--green)"/>
    <path d="M30 0H490C520 80 480 180 390 205C320 222 200 222 130 205C45 180 5 90 30 0Z" fill="var(--white)"/>
    <path d="M60 300C160 370 330 360 520 265V320C350 390 170 395 40 330Z" fill="var(--purple)"/>
    <path d="M40 330C170 395 350 390 520 320V340C350 405 160 405 40 345Z" fill="var(--white)"/>
    <path d="M0 650H330C360 650 370 610 420 612H520V735H0Z" fill="var(--purple)"/>
    <path d="M290 700C300 650 330 635 380 632L520 628V735H290Z" fill="var(--green)"/>
  </svg>

  <div class="brand front-brand">
    <span class="brand__mark"></span>
    Tavistrow Gardening Services
  </div>

  <div class="inset inset--turf" role="img" aria-label="Photo of a gloved hand rolling out fresh turf"></div>
  <div class="inset inset--spreader" role="img" aria-label="Photo of a red lawn fertiliser spreader on grass"></div>

  <h1>
    <span class="headline headline--top">EXPERT LAWN</span>
    <span class="headline headline--bottom">TREATMENT SERVICE</span>
  </h1>

  <p class="offer-pill">Select a one-off treatment or choose from one of<br>our specially created lawn care packages</p>

  <ul class="treatments">
    <li><svg class="treatment-icon" viewBox="0 0 22 22"><circle cx="11" cy="11" r="11" fill="var(--green)"/><rect x="7" y="7" width="8" height="9" rx="1" fill="none" stroke="#fff" stroke-width="1.5"/></svg>Lawn Fertilising</li>
    <li><svg class="treatment-icon" viewBox="0 0 22 22"><circle cx="11" cy="11" r="11" fill="var(--green)"/><path d="M6 12h10M7 15v-3M10 15v-3M13 15v-3M16 15v-3" stroke="#fff" stroke-width="1.4"/></svg>Weed Control</li>
    <li><svg class="treatment-icon" viewBox="0 0 22 22"><circle cx="11" cy="11" r="11" fill="var(--green)"/><path d="M5 15h12M11 15V8M8 15l-2-4M14 15l2-4" stroke="#fff" stroke-width="1.4" fill="none"/></svg>PlumeRest</li>
    <li><svg class="treatment-icon" viewBox="0 0 22 22"><circle cx="11" cy="11" r="11" fill="var(--green)"/><path d="M6 9h10M6 13h10M8 7v8M11 7v8M14 7v8" stroke="#fff" stroke-width="1.2"/></svg>Scarification</li>
    <li><svg class="treatment-icon" viewBox="0 0 22 22"><circle cx="11" cy="11" r="11" fill="var(--green)"/><circle cx="11" cy="11" r="4.5" fill="none" stroke="#fff" stroke-width="1.5"/></svg>Moss Control</li>
    <li><svg class="treatment-icon" viewBox="0 0 22 22"><circle cx="11" cy="11" r="11" fill="var(--green)"/><path d="M6 15l4-4 3 2 4-5" stroke="#fff" stroke-width="1.5" fill="none"/></svg>Turfing &amp; Renovation</li>
    <li><svg class="treatment-icon" viewBox="0 0 22 22"><circle cx="11" cy="11" r="11" fill="var(--green)"/><path d="M11 16V7M11 12l-4-3M11 12l4-3" stroke="#fff" stroke-width="1.5" fill="none"/></svg>Aeration</li>
    <li><svg class="treatment-icon" viewBox="0 0 22 22"><circle cx="11" cy="11" r="11" fill="var(--green)"/><path d="M11 6c3 4 4 6 4 8a4 4 0 0 1-8 0c0-2 1-4 4-8Z" fill="none" stroke="#fff" stroke-width="1.4"/></svg>Hydration Booster</li>
  </ul>

  <div class="contact front-contact">
    <div class="contact__row contact__phone">
      <svg width="14" height="14" viewBox="0 0 14 14"><circle cx="7" cy="7" r="6" fill="none" stroke="#fff" stroke-width="1.2"/><path d="M5 4l1 2-1 1c.5 1 1 1.5 2 2l1-1 2 1-1 1.5C6.5 10.5 3.5 7.5 3.5 5Z" fill="#fff"/></svg>
      01632 960417
    </div>
    <div class="contact__row contact__web">
      <svg width="10" height="10" viewBox="0 0 10 10"><circle cx="5" cy="5" r="4.3" fill="none" stroke="#fff"/><path d="M1 5h8M5 1c-2 2.5-2 5.5 0 8M5 1c2 2.5 2 5.5 0 8" fill="none" stroke="#fff" stroke-width=".7"/></svg>
      www.tavistrowgardening.co.uk/lawncare
    </div>
  </div>
  <p class="strapline">Lawn care by your local<br>gardening expert</p>
  <div class="grass" role="img" aria-label="Close-up of grass blades along the bottom edge"></div>
</section>

<!-- BACK -->
<section class="flyer flyer--back" aria-label="Flyer back">
  <div class="photo back-photo" role="img" aria-label="Photo of a neatly striped lawn beside a paved garden path"></div>

  <svg class="layer" viewBox="0 0 520 735" aria-hidden="true">
    <path d="M0 130C60 190 200 205 330 195C420 188 480 175 520 165V0H520V210C420 220 250 225 120 215C60 210 20 200 0 190Z" fill="var(--purple)"/>
    <path d="M200 0H520V175C440 190 350 198 280 180C200 150 180 60 200 0Z" fill="var(--green)"/>
    <path d="M215 0H520V160C440 178 360 182 300 165C220 140 195 60 215 0Z" fill="var(--white)"/>
    <path d="M0 175C100 205 300 210 520 190V200C300 222 100 220 0 190Z" fill="var(--white)"/>
    <path d="M300 735C300 680 330 655 390 650C450 645 500 640 520 620V735Z" fill="var(--purple)"/>
  </svg>

  <div class="brand back-brand">
    <span class="brand__mark"></span>
    Tavistrow Gardening Services
  </div>

  <div class="about">
    <p>As expert gardeners, we are passionate about horticulture and working to bring out the very best in your garden. When we work in your garden, we look at it and treat it with the same care and attention as if it were our own, before handing it back for you to enjoy. Our passion doesn't end at just trees and shrubs though. Your grass is as much of a living, breathing plant as your shrubs and we therefore utilise our expert horticultural knowledge to ensure your lawn thrives and reaches its fullest potential.</p>
    <p>Lawn care isn't just about applying a fertiliser. It's about really understanding your lawn and being able to use extensive knowledge and experience to diagnose and treat issues. It therefore stands to reason that you should employ an expert to bring out the best in your lawn which is why we at Tavistrow Gardening Services have created a superior lawn care service that will keep your lawn looking lush, green and healthy all year round.</p>
  </div>

  <h2 class="packages-title">LAWN TREATMENT PACKAGES</h2>
  <table class="packages">
    <thead>
      <tr><th>Packages</th><th>Standard Package</th><th>Enhanced Package</th><th>Premium Package</th></tr>
    </thead>
    <tbody>
      <tr><td>Spring Treatment</td><td><svg class="tick" viewBox="0 0 11 9"><path d="M1 5l3 3 6-7" stroke="#fff" stroke-width="2" fill="none"/></svg></td><td><svg class="tick" viewBox="0 0 11 9"><path d="M1 5l3 3 6-7" stroke="#fff" stroke-width="2" fill="none"/></svg></td><td><svg class="tick" viewBox="0 0 11 9"><path d="M1 5l3 3 6-7" stroke="#fff" stroke-width="2" fill="none"/></svg></td></tr>
      <tr><td>Early Summer Treatment</td><td><svg class="tick" viewBox="0 0 11 9"><path d="M1 5l3 3 6-7" stroke="#fff" stroke-width="2" fill="none"/></svg></td><td><svg class="tick" viewBox="0 0 11 9"><path d="M1 5l3 3 6-7" stroke="#fff" stroke-width="2" fill="none"/></svg></td><td><svg class="tick" viewBox="0 0 11 9"><path d="M1 5l3 3 6-7" stroke="#fff" stroke-width="2" fill="none"/></svg></td></tr>
      <tr><td>Late Summer Treatment</td><td><svg class="tick" viewBox="0 0 11 9"><path d="M1 5l3 3 6-7" stroke="#fff" stroke-width="2" fill="none"/></svg></td><td><svg class="tick" viewBox="0 0 11 9"><path d="M1 5l3 3 6-7" stroke="#fff" stroke-width="2" fill="none"/></svg></td><td><svg class="tick" viewBox="0 0 11 9"><path d="M1 5l3 3 6-7" stroke="#fff" stroke-width="2" fill="none"/></svg></td></tr>
      <tr><td>Autumn/Winter Treatment</td><td><svg class="tick" viewBox="0 0 11 9"><path d="M1 5l3 3 6-7" stroke="#fff" stroke-width="2" fill="none"/></svg></td><td><svg class="tick" viewBox="0 0 11 9"><path d="M1 5l3 3 6-7" stroke="#fff" stroke-width="2" fill="none"/></svg></td><td><svg class="tick" viewBox="0 0 11 9"><path d="M1 5l3 3 6-7" stroke="#fff" stroke-width="2" fill="none"/></svg></td></tr>
      <tr><td>Scarification</td><td></td><td><svg class="tick" viewBox="0 0 11 9"><path d="M1 5l3 3 6-7" stroke="#fff" stroke-width="2" fill="none"/></svg></td><td><svg class="tick" viewBox="0 0 11 9"><path d="M1 5l3 3 6-7" stroke="#fff" stroke-width="2" fill="none"/></svg></td></tr>
      <tr><td>Aeration</td><td></td><td></td><td><svg class="tick" viewBox="0 0 11 9"><path d="M1 5l3 3 6-7" stroke="#fff" stroke-width="2" fill="none"/></svg></td></tr>
      <tr><td>PlumeRest Treatment</td><td></td><td></td><td><svg class="tick" viewBox="0 0 11 9"><path d="M1 5l3 3 6-7" stroke="#fff" stroke-width="2" fill="none"/></svg></td></tr>
      <tr><td>Hydration Boost Treatment</td><td></td><td></td><td><svg class="tick" viewBox="0 0 11 9"><path d="M1 5l3 3 6-7" stroke="#fff" stroke-width="2" fill="none"/></svg></td></tr>
    </tbody>
  </table>

  <div class="other-services">
    <h3>The other gardening services we do</h3>
    <ul>
      <li>Lawn mowing</li><li>Shrub pruning</li><li>Hedge trimming</li><li>Weed killing</li>
      <li>Garden clearance &amp; tidy-up</li><li>Planting &amp; design</li><li>Regular Garden Maintenance</li><li>Turfing</li>
      <li>Fencing</li><li>Gutter clearance</li>
    </ul>
  </div>

  <div class="contact back-contact">
    <div class="contact__row contact__phone">
      <svg width="16" height="16" viewBox="0 0 14 14"><circle cx="7" cy="7" r="6" fill="none" stroke="#fff" stroke-width="1.2"/><path d="M5 4l1 2-1 1c.5 1 1 1.5 2 2l1-1 2 1-1 1.5C6.5 10.5 3.5 7.5 3.5 5Z" fill="#fff"/></svg>
      01632 960417
    </div>
    <div class="contact__row contact__web">
      <svg width="10" height="10" viewBox="0 0 10 10"><circle cx="5" cy="5" r="4.3" fill="none" stroke="#fff"/><path d="M1 5h8M5 1c-2 2.5-2 5.5 0 8M5 1c2 2.5 2 5.5 0 8" fill="none" stroke="#fff" stroke-width=".7"/></svg>
      www.tavistrowgardening.co.uk/lawncare
    </div>
  </div>
  <div class="grass grass--back" role="img" aria-label="Close-up of grass blades along the bottom edge"></div>
</section>

</body>
</html>
```